Process Diagram - Circular Economy

I would like for a designer to take this rough sketch and turn it into a high quality design which can be used in a business presentation. Seeking to get both PDF and Jpeg file versions of the finished product.

Colours don't have to be the exact same as the rough sketch PDF, the green used is pretty ugly so open to some changes.

Target Market(s)

Corporate audience

Requirements
Must have
• Clear text for each party; VENOR, ORVANE, BUYER

Smaller text for the functions; marketing, recovery, logistics, cleaning, decontamination, testing & re-certification, storage, engineering suitability

```html
<!DOCTYPE html>
<html lang="en">
<head>
<meta charset="utf-8">
<title>Circular Economy Process</title>
<link rel="stylesheet" href="https://fonts.googleapis.com/css2?family=Roboto:ital,wght@0,500;0,700;1,500&family=Roboto+Slab:wght@700&display=swap">
<style>
  :root {
    --ink: #454545;
    --paper: #ffffff;
    --vendor-blue: #236ea0;
    --buyer-green: #4fbf8e;
    --hub-orange: #da6944;
    --marketing-coral: #d97c5c;
    --label: #ffffff;
  }
  html, body {
    margin: 0;
    padding: 0;
    width: 1200px;
    height: 832px;
    overflow: hidden;
    background: var(--paper);
  }
  .process-diagram {
    display: block;
    width: 1200px;
    height: 832px;
  }
  .stage-title {
    font-family: "Roboto", Arial, sans-serif;
    font-weight: 700;
    font-size: 44px;
    fill: var(--ink);
  }
  .party-name {
    font-family: "Roboto Slab", "Rockwell", Georgia, serif;
    font-weight: 700;
    font-size: 31px;
    fill: var(--label);
  }
  .function-label {
    font-family: "Roboto", Arial, sans-serif;
    font-weight: 500;
    font-size: 19px;
    fill: var(--label);
  }
  .function-label--italic { font-style: italic; }
  .buyer-arrow { fill: var(--buyer-green); }
  .marketing-band { fill: var(--marketing-coral); }
</style>
</head>
<body>
<svg class="process-diagram" viewBox="0 0 1600 1109" xmlns="http://www.w3.org/2000/svg" role="img" aria-label="Circular economy process from vendor through Orvane to buyer">
  <defs>
    <linearGradient id="ring-fill" gradientUnits="userSpaceOnUse" x1="640" y1="0" x2="880" y2="0">
      <stop offset="0" stop-color="var(--buyer-green)"/>
      <stop offset="1" stop-color="var(--hub-orange)"/>
    </linearGradient>
    <linearGradient id="vendor-fill" gradientUnits="userSpaceOnUse" x1="690" y1="420" x2="960" y2="520">
      <stop offset="0" stop-color="var(--vendor-blue)"/>
      <stop offset="0.4" stop-color="#5a6c92"/>
      <stop offset="1" stop-color="var(--hub-orange)"/>
    </linearGradient>
  </defs>

  <text class="stage-title" x="157" y="201">END OF LIFE</text>
  <text class="stage-title" x="1448" y="201" text-anchor="end">NEW LIFE</text>

  <polygon class="buyer-arrow" points="810,395 1303,268 1433,296 1303,398 1000,482"/>

  <path class="hub-ring" fill="url(#ring-fill)" fill-rule="evenodd"
        d="M1084,680 A274,274 0 1 1 536,680 A274,274 0 1 1 1084,680 Z
           M956,680 A146,146 0 1 0 664,680 A146,146 0 1 0 956,680 Z"/>

  <path class="vendor-band" fill="url(#vendor-fill)"
        d="M158,268 L870,408 Q960,432 1000,483 L910,570 Q830,492 700,470 L158,398 Z"/>

  <path class="marketing-band"
        d="M240,383 L700,470 Q860,500 910,570 Q942,605 955,645 Q880,600 730,550 L240,448 Z"/>

  <text class="party-name" x="188" y="353">VENDOR</text>
  <text class="party-name" x="1212" y="346">BUYER</text>
  <text class="party-name" x="920" y="803">ORVANE</text>

  <text class="function-label function-label--italic" x="254" y="425" transform="rotate(12 254 425)">Marketing</text>
  <text class="function-label" x="768" y="462">Recovery</text>
  <text class="function-label" x="957" y="592">Logistics</text>
  <text class="function-label" x="977" y="696">Cleaning</text>
  <text class="function-label" x="727" y="889">Decontamination</text>
  <text class="function-label" x="567" y="773">Testing &amp;</text>
  <text class="function-label" x="567" y="799">Re-certification</text>
  <text class="function-label" x="561" y="696">Storage</text>
  <text class="function-label" x="568" y="580">Engineering</text>
  <text class="function-label" x="568" y="605">Suitability</text>
</svg>
</body>
</html>
```